Camp Maplebrook Summer Programs Postcard

We need a postcard design for summer 2017 programs. Camp Maplebrook offers nine weeks of day camp and one week of overnight camp. We are a Christian summer camp. We offer lots of activities like swimming, archery, rock wall, zipline, sports, crafts, drama and more. We want to showcase the activities we offer. The design should communicate outdoor fun and friendship. We want to focus on high quality photos that reflect the activities we offer.

Target Market(s)

Elementary age children/parents

Industry/Entity Type

Childcare

Font styles to use
Serif

Requirements
Must have
• Camp Maplebrook "Christian Camping Since 1952"
• Day Camp 2017 "Courageous Campers"
• June 19 - August 18
• $130 per week
• Mon-Fri 8 am to 4 pm. Open to all kids entering grades 1 to 8. Day camp is chock full of activities like swimming, rock wall, archery, zipline, sports, campfires and much more! Daily lunch and snack included. Before and after-care available at an extra rate.
• Overnight Camp 2017
• July 16 - 22
• $325
• Open to all kids ages 8 to 14. Spend the week making new friends, sleeping in cabins, climbing the rock wall and ziplining under the stars! Our special guest speaker will lead twice daily chapel sessions that will challenge campers to grow in their faith.
• Register and pay for 7 weeks by May 1st, get 2 FREE!
• Website: www.maplebrook-example.org
• Address: 42 Cedar Vale Rd. Dunmore, NH 03990
• Phone: 603-555-0148

```html
<!DOCTYPE html>
<html lang="en">
<head>
<meta charset="utf-8">
<title>Camp Maplebrook Summer Programs Postcard</title>
<link href="https://fonts.googleapis.com/css2?family=Arvo:wght@700&family=Mulish:ital,wght@0,400;0,700;0,800;1,400;1,600&display=swap" rel="stylesheet">
<style>
  :root {
    --backdrop: #e4e4e4;
    --card-orange: #d0472e;
    --camp-red: #c01f2e;
    --promo-orange: #cc4a2a;
    --logo-brown: #6b3a1e;
    --ink: #2e2e2e;
    --white: #ffffff;
    --band-pink: #f7e3e0;
  }
  * { box-sizing: border-box; margin: 0; padding: 0; }
  html, body { width: 1200px; height: 1200px; overflow: hidden; background: var(--backdrop); }
  body { position: relative; font-family: "Mulish", Arial, sans-serif; }

  .postcard {
    position: absolute; left: 85px; top: 232px;
    width: 1288px; height: 920px;
    transform: scale(0.8); transform-origin: 0 0;
    background: var(--card-orange);
    overflow: hidden;
  }
  .panel-shape { position: absolute; inset: 0; }

  .tagline {
    position: absolute; left: 168px; top: 34px; width: 456px; height: 104px;
    background: var(--camp-red); border-radius: 4px 4px 10px 10px;
    transform: rotate(-1deg);
    font-family: "Arvo", Georgia, serif; color: var(--white);
    font-size: 34px; line-height: 40px; text-align: center; padding-top: 14px;
  }

  .photo {
    position: absolute; border: 7px solid var(--white); border-radius: 22px;
    box-shadow: 0 2px 6px rgba(0,0,0,.12);
  }
  .photo--climb-tree { left: 72px; top: 128px; width: 292px; height: 292px; transform: rotate(5deg);
    background: linear-gradient(160deg, #9fc46a, #3f6a2a 70%, #5a4a3a); }
  .photo--friends { left: 384px; top: 198px; width: 232px; height: 240px; transform: rotate(5deg);
    background: linear-gradient(150deg, #e8a24a, #8a5a5a 55%, #3a3a4a); }
  .photo--rock-wall { left: 86px; top: 440px; width: 240px; height: 245px; transform: rotate(4deg);
    background: linear-gradient(100deg, #cfdcdc 45%, #5f8a3a 60%, #2f5a22); }
  .photo--paddle-boat { left: 348px; top: 446px; width: 240px; height: 240px; transform: rotate(4deg);
    background: linear-gradient(180deg, #3a4a5a, #5a6a6a 40%, #d8443a 62%, #f0d830 85%); }

  .brand {
    position: absolute; left: 735px; top: 96px;
    display: flex; align-items: center; gap: 20px;
  }
  .brand-dot { width: 58px; height: 58px; border-radius: 50%; background: var(--camp-red); }
  .brand-name {
    font-weight: 800; color: var(--logo-brown);
    font-size: 58px; line-height: 60px; letter-spacing: -0.5px;
  }

  .program-band {
    position: absolute; left: 596px; width: 560px; height: 66px;
    background: linear-gradient(90deg, rgba(247,227,224,0) 0%, var(--band-pink) 12%, var(--band-pink) 70%, rgba(247,227,224,0) 100%);
  }
  .program {
    position: absolute; left: 672px; width: 500px; color: var(--ink);
  }
  .program-title { color: var(--promo-orange); font-weight: 700; font-size: 23px; line-height: 30px; }
  .program-dates { font-style: italic; font-weight: 600; font-size: 21px; line-height: 28px; color: var(--ink); }
  .program-copy { margin-top: 10px; font-size: 16px; line-height: 21.3px; }
  .program-copy strong { font-weight: 800; }
  .program-price { color: var(--camp-red); font-weight: 800; font-size: 23px; line-height: 30px; margin-top: 6px; }

  .day-band { top: 280px; }
  .day-camp { top: 284px; }
  .overnight-band { top: 505px; }
  .overnight-camp { top: 508px; }

  .promo {
    position: absolute; left: 150px; top: 700px; width: 470px;
    text-align: center; color: var(--camp-red); transform: rotate(3deg);
  }
  .promo-line { font-weight: 800; font-size: 21px; line-height: 28px; }
  .promo-offer { color: var(--promo-orange); font-weight: 800; font-size: 36px; line-height: 44px; }

  .phone {
    position: absolute; left: 648px; top: 752px; width: 458px; height: 112px;
    background: var(--camp-red); border-radius: 14px 14px 0 0;
    transform: rotate(2deg);
    color: var(--white); font-weight: 800; font-size: 46px; text-align: center; padding-top: 20px;
  }

  .footer {
    position: absolute; left: 42px; top: 866px;
    color: var(--white); font-size: 20px; display: flex; gap: 32px;
  }
  .footer strong { font-weight: 800; }
</style>
</head>
<body>
  <main class="postcard">
    <svg class="panel-shape" viewBox="0 0 1288 920" width="1288" height="920" aria-hidden="true">
      <path d="M170 65 L1130 40 Q1235 38 1232 140 L1195 760 Q1188 862 1090 860 L190 805 Q90 798 92 700 L92 170 Q95 68 170 65 Z"
            fill="#ffffff" stroke="#c01f2e" stroke-width="5"/>
      <path d="M176 80 L1128 56 Q1218 55 1216 142 L1180 756 Q1174 845 1090 844 L192 790 Q106 784 108 700 L108 172 Q110 82 176 80 Z"
            fill="none" stroke="#c01f2e" stroke-width="1.5" stroke-dasharray="12 8"/>
    </svg>

    <div class="tagline">Christian Camping<br>Since 1952</div>

    <div class="photo photo--climb-tree" role="img" aria-label="Photo of a camper in a helmet climbing a rope in the trees"></div>
    <div class="photo photo--friends" role="img" aria-label="Photo of two smiling camp friends"></div>
    <div class="photo photo--rock-wall" role="img" aria-label="Photo of a camper climbing the rock wall"></div>
    <div class="photo photo--paddle-boat" role="img" aria-label="Photo of campers in life jackets on a paddle boat"></div>

    <div class="brand">
      <span class="brand-dot"></span>
      <div class="brand-name">Camp<br>Maplebrook</div>
    </div>

    <div class="program-band day-band"></div>
    <section class="program day-camp">
      <h2 class="program-title">Day Camp 2017 "Courageous Campers"</h2>
      <p class="program-dates">June 19 - August 18</p>
      <p class="program-copy">Mon-Fri 8 am to 4 pm. <strong>Open to all kids entering grades 1 to 8.</strong><br>
        Day camp is chock full of activities like swimming, rock wall,<br>
        archery, zipline, sports, campfires and much more!<br>
        Daily lunch and snack included.<br>
        Before and after-care available at an extra rate.</p>
      <p class="program-price">$130 per week</p>
    </section>

    <div class="program-band overnight-band"></div>
    <section class="program overnight-camp">
      <h2 class="program-title">Overnight Camp 2017</h2>
      <p class="program-dates">July 16 - 22</p>
      <p class="program-copy"><strong>Open to all kids ages 8 to 14.</strong><br>
        Spend the week making new friends, sleeping in cabins,<br>
        climbing the rock wall and ziplining under the stars!<br>
        Our special guest speaker will lead twice daily<br>
        chapel sessions that will challenge campers to grow in<br>
        their faith.</p>
      <p class="program-price">$325</p>
    </section>

    <div class="promo">
      <p class="promo-line">Register and pay for 7 weeks by May 1st,</p>
      <p class="promo-offer">get 2 FREE!</p>
    </div>

    <div class="phone">603-555-0148</div>

    <footer class="footer">
      <span><strong>Website:</strong> www.maplebrook-example.org</span>
      <span><strong>Address:</strong> 42 Cedar Vale Rd. Dunmore, NH 03990</span>
    </footer>
  </main>
</body>
</html>
```